Tranquil Renewal

Medical doctor providing aesthetic medicine

* Double sided card
* Logo to be on card
Other details:
* Dr. Halvard Meckin, BSc, MBChB, CCFP
* #214-215, 27394 83 Ave, Surrey, BC, V4T 2K7
* 604-718-2453
* info@calmbrookclinic.ca
* www.calmbrookclinic.ca

Industry/Entity Type

Medical / Health & Beauty

Contact Information for Business Card

see 'Project Description'

Colors
0054AA
0677BA
7BADD7
CADEEF
E8F1F8
FFF300
FFF600
FEFA6F
FFFEC7
FFFEE8

Requirements
Must have
• Modern, high-end design

```html
<!DOCTYPE html>
<html lang="en">
<head>
<meta charset="utf-8">
<title>Tranquil Renewal — Business Card</title>
<link rel="stylesheet" href="https://fonts.googleapis.com/css2?family=Montserrat:wght@400;500;600&display=swap">
<style>
  :root {
    --stage: #3a3a3a;
    --card-dark: #050505;
    --card-light: #ffffff;
    --gold: #c9a227;
    --ink: #111111;
    --muted: #2b2b2b;
    --on-dark: #f2f2f2;
  }
  * { margin: 0; padding: 0; box-sizing: border-box; }
  html, body { width: 1200px; height: 900px; overflow: hidden; }
  body {
    background: var(--stage);
    font-family: "Montserrat", Arial, sans-serif;
    display: flex;
    flex-direction: column;
    align-items: center;
    justify-content: center;
    gap: 40px;
  }
  .card {
    width: 700px;
    height: 400px;
    position: relative;
    box-shadow: 0 10px 30px rgba(0,0,0,0.45);
  }

  /* Brand name: plain single-line text in the card's own type */
  .brand-name {
    font-weight: 500;
    line-height: 1;
    letter-spacing: 0.02em;
    white-space: nowrap;
  }

  /* Front */
  .card-front {
    background: var(--card-dark);
    display: flex;
    align-items: center;
    justify-content: center;
  }
  .card-front .brand-name {
    color: var(--on-dark);
    font-size: 42px;
  }

  /* Back */
  .card-back { background: var(--card-light); }
  .card-back .brand-name {
    position: absolute;
    top: 82px;
    right: 52px;
    color: var(--ink);
    font-size: 46px;
  }
  .doctor {
    position: absolute;
    left: 52px;
    top: 250px;
    width: 250px;
    text-align: right;
  }
  .doctor-name {
    color: var(--gold);
    font-weight: 600;
    font-size: 22px;
    white-space: nowrap;
  }
  .doctor-creds {
    color: var(--muted);
    font-size: 13px;
    margin-top: 4px;
  }
  .divider {
    position: absolute;
    left: 322px;
    top: 236px;
    width: 2px;
    height: 86px;
    background: var(--gold);
  }
  .contact-list {
    position: absolute;
    left: 342px;
    top: 236px;
    list-style: none;
    font-size: 14px;
    color: var(--muted);
  }
  .contact-list li {
    display: flex;
    align-items: center;
    gap: 10px;
    height: 29px;
  }
  .contact-list svg { width: 14px; height: 14px; fill: var(--gold); flex: none; }
  .address {
    position: absolute;
    left: 0; right: 0;
    bottom: 36px;
    text-align: center;
    font-size: 14px;
    color: var(--ink);
  }
</style>
</head>
<body>
  <section class="card card-front">
    <p class="brand-name">Tranquil Renewal</p>
  </section>

  <section class="card card-back">
    <p class="brand-name">Tranquil Renewal</p>

    <div class="doctor">
      <p class="doctor-name">Dr. Halvard Meckin</p>
      <p class="doctor-creds">BSc, MBChB, CCFP</p>
    </div>

    <div class="divider"></div>

    <ul class="contact-list">
      <li>
        <svg viewBox="0 0 24 24" aria-hidden="true"><path d="M6.6 10.8a15.1 15.1 0 0 0 6.6 6.6l2.2-2.2a1 1 0 0 1 1-.25 11.4 11.4 0 0 0 3.6.57 1 1 0 0 1 1 1V20a1 1 0 0 1-1 1A17 17 0 0 1 3 4a1 1 0 0 1 1-1h3.5a1 1 0 0 1 1 1c0 1.25.2 2.45.57 3.57a1 1 0 0 1-.25 1z"/></svg>
        <span>604-718-2453</span>
      </li>
      <li>
        <svg viewBox="0 0 24 24" aria-hidden="true"><path d="M2 5h20v14H2z M2 5l10 8 10-8"/></svg>
        <span>info@calmbrookclinic.ca</span>
      </li>
      <li>
        <svg viewBox="0 0 24 24" aria-hidden="true"><path d="M12 2a10 10 0 1 0 0 20 10 10 0 0 0 0-20zm0 2.2c.9 1.2 1.6 2.6 2 4.3h-4c.4-1.7 1.1-3.1 2-4.3zM4.4 14a8 8 0 0 1 0-4h3.4a16 16 0 0 0 0 4zm.8 2h3c.4 1.5 1 2.8 1.7 3.9A8 8 0 0 1 5.2 16zm3-8h-3a8 8 0 0 1 4.7-3.9C9.2 5.2 8.6 6.5 8.2 8zM12 19.8c-.9-1.2-1.6-2.6-2-4.3h4c-.4 1.7-1.1 3.1-2 4.3zM14.3 14H9.7a14 14 0 0 1 0-4h4.6a14 14 0 0 1 0 4zm.3 5.9c.7-1.1 1.3-2.4 1.7-3.9h3a8 8 0 0 1-4.7 3.9zM16.2 14a16 16 0 0 0 0-4h3.4a8 8 0 0 1 0 4zm.6-6c-.4-1.5-1-2.8-1.7-3.9A8 8 0 0 1 19.8 8z"/></svg>
        <span>www.calmbrookclinic.ca</span>
      </li>
    </ul>

    <p class="address">#214-215, 27394 83 Ave, Surrey, BC, V4T 2K7</p>
  </section>
</body>
</html>
```